Brimvantel

We are re-branding the company with a new logo (attached) which I would
like to go on one side of the card, and I have attached a file showing what
the old back side looked like, and I do like the characters that show the
phone, e-mails, etc., I don't like the current arrangement, and I want
something clean, clear and out of the box, as we are an aviation consulting
firm, and we work outside of the box.

```html
<!DOCTYPE html>
<html lang="en">
<head>
<meta charset="utf-8">
<title>Brimvantel – Business Card</title>
<link href="https://fonts.googleapis.com/css2?family=Open+Sans:ital,wght@0,400;0,600;0,700;1,400&display=swap" rel="stylesheet">
<style>
  :root{
    --bg:#d9d9d9;
    --card:#ffffff;
    --ink:#2f2f31;
    --band-dark:#4a4a4d;
    --band-light:#ececec;
    --title:#4f6074;
    --accent:#a8232a;
    --muted:#8a8a8a;
    --rule:#c9c9c9;
  }
  *{box-sizing:border-box;margin:0;padding:0}
  html,body{width:1200px;height:1005px;overflow:hidden}
  body{background:var(--bg);font-family:"Open Sans",Arial,sans-serif;color:var(--ink);position:relative}
  .card{position:absolute;left:215px;width:770px;height:440px;background:var(--card);box-shadow:0 6px 18px rgba(0,0,0,.18);overflow:hidden}
  .card--front{top:40px}
  .card--back{top:525px}

  /* brand lockup */
  .brand{display:flex;flex-direction:column;align-items:center}
  .brand__row{display:flex;align-items:center;gap:14px}
  .brand__dot{width:34px;height:34px;border-radius:50%;background:var(--accent)}
  .brand__name{font-weight:600;font-size:46px;letter-spacing:2px;color:var(--ink);line-height:1}
  .brand__tagline{font-style:italic;font-size:13px;color:var(--muted);margin-top:6px;letter-spacing:.5px}

  .card--front .brand{position:absolute;left:0;right:0;top:145px}
  .front__web{position:absolute;left:0;right:0;top:268px;text-align:center;font-size:18px;color:var(--ink)}

  /* back */
  .back__band{position:absolute;left:0;top:0}
  .back__name{position:absolute;left:26px;top:56px;color:#fff;font-weight:700;font-size:24px;letter-spacing:1px}
  .back__title{position:absolute;left:330px;top:70px;color:var(--title);font-weight:600;font-size:19px}
  .contacts{position:absolute;left:28px;top:140px;list-style:none;width:420px}
  .contact{display:flex;align-items:flex-start;gap:34px;position:relative;margin-bottom:22px}
  .contact::after{content:"";position:absolute;left:-28px;top:calc(100% + 10px);width:86px;height:1px;background:var(--rule)}
  .contact:last-child::after{display:none}
  .contact__icon{width:26px;height:26px;flex:none;fill:var(--ink)}
  .contact__text{font-size:18px;line-height:1.25;color:var(--ink)}
  .card--back .brand{position:absolute;right:50px;top:330px}
  .card--back .brand__name{font-size:40px}
  .card--back .brand__dot{width:28px;height:28px}
</style>
</head>
<body>

<section class="card card--front" aria-label="Card front">
  <div class="brand">
    <div class="brand__row"><span class="brand__dot"></span><span class="brand__name">BRIMVANTEL</span></div>
    <p class="brand__tagline">clear guidance • steady ascent</p>
  </div>
  <p class="front__web">www.brimvantel.com</p>
</section>

<section class="card card--back" aria-label="Card back">
  <svg class="back__band" width="770" height="130" viewBox="0 0 770 130">
    <rect x="0" y="48" width="770" height="52" fill="var(--band-light)"/>
    <polygon points="0,48 290,48 314,100 770,100 770,116 0,116" fill="var(--band-dark)"/>
  </svg>
  <h1 class="back__name">MARCUS HALE</h1>
  <p class="back__title">Managing Director</p>

  <ul class="contacts">
    <li class="contact">
      <svg class="contact__icon" viewBox="0 0 24 24"><path d="M12 2a7 7 0 0 0-7 7c0 5 7 13 7 13s7-8 7-13a7 7 0 0 0-7-7zm0 9.5A2.5 2.5 0 1 1 12 6.5a2.5 2.5 0 0 1 0 5z"/></svg>
      <span class="contact__text">27 Harbor Court, Level 4<br>Kestrel Road KTN</span>
    </li>
    <li class="contact">
      <svg class="contact__icon" viewBox="0 0 24 24"><path d="M6.6 10.8a15 15 0 0 0 6.6 6.6l2.2-2.2a1 1 0 0 1 1-.25 11.4 11.4 0 0 0 3.6.6 1 1 0 0 1 1 1V20a1 1 0 0 1-1 1A17 17 0 0 1 3 4a1 1 0 0 1 1-1h3.5a1 1 0 0 1 1 1c0 1.250.2 2.450.6 3.6a1 1 0 0 1-.25 1z"/></svg>
      <span class="contact__text">014 555 0182<br>014 555 0183</span>
    </li>
    <li class="contact">
      <svg class="contact__icon" viewBox="0 0 24 24"><path d="M2 5h20v14H2zm2 2v.5l8 5.5 8-5.5V7zm0 2.9V17h16V9.9l-8 5.5z"/></svg>
      <span class="contact__text">marcus@brimvantel.com</span>
    </li>
    <li class="contact">
      <svg class="contact__icon" viewBox="0 0 24 24"><path d="M12 2a10 10 0 1 0 0 20 10 10 0 0 0 0-20zm6.9 6h-3a15 15 0 0 0-1.3-3.9A8 8 0 0 1 18.9 8zM12 4c.9 1.2 1.6 2.6 2 4h-4c.4-1.4 1.1-2.8 2-4zM4.3 14a8 8 0 0 1 0-4h3.4a16 16 0 0 0 0 4zm.8 2h3a15 15 0 0 0 1.3 3.9A8 8 0 0 1 5.1 16zm3-8h-3a8 8 0 0 1 4.3-3.9A15 15 0 0 0 8.1 8zM12 20c-.9-1.2-1.6-2.6-2-4h4c-.4 1.4-1.1 2.8-2 4zm2.3-6H9.7a14 14 0 0 1 0-4h4.6a14 14 0 0 1 0 4zm.3 5.9a15 15 0 0 0 1.3-3.9h3a8 8 0 0 1-4.3 3.9zm1.7-5.9a16 16 0 0 0 0-4h3.4a8 8 0 0 1 0 4z"/></svg>
      <span class="contact__text">www.brimvantel.com</span>
    </li>
  </ul>

  <div class="brand">
    <div class="brand__row"><span class="brand__dot"></span><span class="brand__name">BRIMVANTEL</span></div>
    <p class="brand__tagline">clear guidance • steady ascent</p>
  </div>
</section>

</body>
</html>
```